A Clear Three Step Roadmap For Contractors

We are looking for a one-pager "roadmap" that is similar to the 2nd picture we attached, but much more professional & better... please make it landscape orientation. The logo for this system is attached below, as well.

Our Brand Colors to use:
#f2d582
#303030
#8b8c90

The copy we'd like to use on the flyer:
A Clear Three Step Roadmap that will finally allow you to attract quality customers and win more jobs.

The Keystone Ladder Method is a simple to follow system that was created specifically for Contractors and Blue Collar Business Owners.

When it comes to marketing and growing their business, the majority of Contractors are left confused, frustrated and extremely overwhelmed. Unlike most sales, marketing & training programs that offer a single "piece of the puzzle", we've mapped out each essential step of the puzzle and cut out all of the fluff.

All you have to do is complete each step in the right order and we'll be guiding you along the entire journey!

A ---> B

Blueprint: Get clear on where you're going, define your ideal audience, and finally, master your message.
Step 1: Clarify The Chaos
Step 2: Define Your Customer
Step 3: Master Your Message

Build: Attract quality leads, Build your funnel and Formulate a high-converting follow-up system
Step 4: Develop Lead Generator
Step 5: Construct Your Funnel
Step 6: Formulate the Follow-Up

Breakthrough: Get in front of your ideal customers and rapidly scale your business by driving traffic and becoming the authority in your market
Step 7: Turn-On the Traffic
Step 8: Become the Authority
Step 9: Unlock Your Growth

```html
<!DOCTYPE html>
<html lang="en">
<head>
<meta charset="utf-8">
<title>Keystone Ladder Method – Three Step Roadmap</title>
<link rel="stylesheet" href="https://fonts.googleapis.com/css2?family=Oswald:wght@500&family=Roboto:wght@500;700&display=swap">
<style>
  :root {
    --brand-yellow: #f2d582;
    --brand-yellow-soft: #f7e3a6;
    --brand-dark: #303030;
    --brand-grey: #8b8c90;
    --ink: #1e1e1e;
    --paper: #ffffff;
    --backdrop: #f1f1f1;
  }
  * { box-sizing: border-box; margin: 0; padding: 0; }
  html, body { width: 713px; height: 1200px; overflow: hidden; background: var(--backdrop); }
  .roadmap {
    position: absolute; left: 30px; top: 347px;
    width: 653px; height: 506px;
    background: linear-gradient(135deg, #ffffff 0%, #f7f7f5 60%, #f3f3f1 100%);
    box-shadow: -14px 14px 0 rgba(0,0,0,0.22);
    overflow: hidden;
  }
  .road-art { position: absolute; left: 0; top: 0; width: 653px; height: 506px; }
  .step-pin { position: absolute; width: 56px; height: 70px; }
  .step-pin svg { position: absolute; left: 0; top: 0; }
  .step-pin .pin-label {
    position: absolute; left: 0; top: 19px; width: 56px; text-align: center;
    font: 500 13px/14px "Oswald", sans-serif; color: var(--brand-dark);
  }
  .step-title {
    position: absolute;
    font: 500 11.5px/15px "Oswald", sans-serif; color: var(--ink);
    text-transform: uppercase; letter-spacing: 0.1px; white-space: nowrap;
  }
  .step-rule { position: absolute; height: 1.5px; background: var(--brand-dark); }
  .step-rule::after {
    content: ""; position: absolute; right: -2px; top: -2px; width: 6px; height: 1.5px;
    background: var(--brand-dark); transform: rotate(30deg);
  }
  .task-icon {
    position: absolute; width: 35px; height: 35px; border-radius: 50%;
    background: var(--brand-yellow);
    box-shadow: 0 0 0 3px var(--brand-yellow-soft);
  }
  .task-icon svg { width: 35px; height: 35px; }
  .task-label {
    position: absolute;
    font: 500 9.2px/11px "Roboto", sans-serif; color: var(--ink); white-space: nowrap;
  }
  .brand-mark { position: absolute; left: 425px; top: 436px; width: 36px; height: 36px; background: var(--brand-yellow); }
  .brand-name {
    position: absolute; left: 470px; top: 434px;
    font: 700 17px/20px "Roboto", sans-serif; color: var(--brand-dark);
    text-transform: uppercase; letter-spacing: 0.3px;
  }
</style>
</head>
<body>
<main class="roadmap">

  <svg class="road-art" viewBox="0 0 653 506" role="img" aria-label="Illustration of a winding asphalt road curving from the top left towards the bottom, beside a yellow field">
    <defs>
      <linearGradient id="roadShade" x1="0" y1="0" x2="0" y2="1">
        <stop offset="0" stop-color="#3a3a3a"/>
        <stop offset="0.6" stop-color="#1c1c1c"/>
        <stop offset="1" stop-color="#050505"/>
      </linearGradient>
    </defs>
    <path d="M0,0 L80,0 C55,22 70,42 140,58 C255,88 292,150 318,235 L402,506 L0,506 Z" fill="url(#roadShade)"/>
  </svg>

  <!-- Step 1 -->
  <div class="step-pin" style="left:178px;top:25px">
    <svg width="56" height="70" viewBox="0 0 56 70"><path d="M28,66 L8,40 A26,26 0 1 1 48,40 Z" fill="var(--brand-yellow)"/><circle cx="28" cy="26" r="20" fill="#fff"/></svg>
    <span class="pin-label">STEP 1</span>
  </div>
  <p class="step-title" style="left:250px;top:36px">Get clear on where you're going, define<br>your ideal audience, and finally, master your message.</p>
  <div class="step-rule" style="left:223px;top:71px;width:398px"></div>

  <div class="task-icon" style="left:278px;top:80px"><svg viewBox="0 0 35 35" fill="none" stroke="#303030" stroke-width="1.4"><circle cx="20" cy="15" r="6"/><path d="M15.5 19.5 L10 25"/></svg></div>
  <p class="task-label" style="left:319px;top:87px">Clarify<br>The Chaos</p>
  <div class="task-icon" style="left:384px;top:80px"><svg viewBox="0 0 35 35" fill="none" stroke="#303030" stroke-width="1.3"><rect x="11" y="9" width="13" height="17" rx="1"/><path d="M14 13h7M14 16h7M14 19h4"/><circle cx="21" cy="21" r="3"/></svg></div>
  <p class="task-label" style="left:424px;top:87px">Define<br>Your Customer</p>
  <div class="task-icon" style="left:497px;top:80px"><svg viewBox="0 0 35 35" fill="none" stroke="#303030" stroke-width="1.4"><path d="M9 11h17v11H15l-4 3v-3H9z"/><path d="M12 15h11M12 18h11"/></svg></div>
  <p class="task-label" style="left:544px;top:87px">Master<br>Your Message</p>

  <!-- Step 2 -->
  <div class="step-pin" style="left:259px;top:140px">
    <svg width="56" height="70" viewBox="0 0 56 70"><path d="M28,66 L8,40 A26,26 0 1 1 48,40 Z" fill="var(--brand-yellow)"/><circle cx="28" cy="26" r="20" fill="#fff"/></svg>
    <span class="pin-label">STEP 2</span>
  </div>
  <p class="step-title" style="left:326px;top:151px">Attract quality leads, build your funnel and<br>formulate a high-converting follow-up system</p>
  <div class="step-rule" style="left:302px;top:192px;width:319px"></div>

  <div class="task-icon" style="left:322px;top:201px"><svg viewBox="0 0 35 35" fill="none" stroke="#303030" stroke-width="1.3"><circle cx="17.5" cy="13" r="4"/><path d="M11 26c0-5 3-7 6.5-7s6.5 2 6.5 7"/></svg></div>
  <p class="task-label" style="left:363px;top:208px">Develop<br>Lead Generator</p>
  <div class="task-icon" style="left:429px;top:201px"><svg viewBox="0 0 35 35" fill="none" stroke="#303030" stroke-width="1.4"><path d="M9 11h17l-6.5 7v7l-4-2v-5z"/></svg></div>
  <p class="task-label" style="left:468px;top:208px">Construct<br>Your Funnel</p>
  <div class="task-icon" style="left:522px;top:201px"><svg viewBox="0 0 35 35" fill="none" stroke="#303030" stroke-width="1.3"><circle cx="12" cy="12" r="3"/><circle cx="23" cy="15" r="3"/><circle cx="16" cy="24" r="3"/><path d="M15 12.5l5 2M21.5 17.5l-4 4M13 15l2 6"/></svg></div>
  <p class="task-label" style="left:563px;top:206px">Formulate<br>the Follow-Up</p>

  <!-- Step 3 -->
  <div class="step-pin" style="left:297px;top:278px">
    <svg width="56" height="70" viewBox="0 0 56 70"><path d="M28,66 L8,40 A26,26 0 1 1 48,40 Z" fill="var(--brand-yellow)"/><circle cx="28" cy="26" r="20" fill="#fff"/></svg>
    <span class="pin-label">STEP 3</span>
  </div>
  <p class="step-title" style="left:367px;top:286px">Get in front of your ideal customers and rapidly<br>scale your business &nbsp;by driving traffic and<br>becoming the authority in your market</p>
  <div class="step-rule" style="left:340px;top:338px;width:281px"></div>

  <div class="task-icon" style="left:363px;top:353px"><svg viewBox="0 0 35 35" fill="none" stroke="#303030" stroke-width="1.3"><path d="M17.5 7l5 8h-10z"/><path d="M17.5 10v3"/><rect x="9" y="18" width="17" height="6" rx="2"/><circle cx="13" cy="26" r="1.5"/><circle cx="22" cy="26" r="1.5"/></svg></div>
  <p class="task-label" style="left:402px;top:360px">Turn-On<br>the Traffic</p>
  <div class="task-icon" style="left:450px;top:353px"><svg viewBox="0 0 35 35" fill="none" stroke="#303030" stroke-width="1.3"><rect x="11" y="8" width="13" height="19" rx="1"/><path d="M17.5 11l3 1.2v2.3c0 2-1.5 3-3 3.5-1.5-.5-3-1.5-3-3.5v-2.3z"/><path d="M14 21h7M14 24h5"/></svg></div>
  <p class="task-label" style="left:487px;top:360px">Become<br>the Authority</p>
  <div class="task-icon" style="left:543px;top:353px"><svg viewBox="0 0 35 35" fill="none" stroke="#303030" stroke-width="1.5"><rect x="11" y="16" width="13" height="10" rx="1.5"/><path d="M13.5 16v-3a4 4 0 0 1 8 0"/><circle cx="17.5" cy="21" r="1.2" fill="#303030"/></svg></div>
  <p class="task-label" style="left:582px;top:358px">Unlock<br>Your Growth</p>

  <!-- Brand -->
  <div class="brand-mark"></div>
  <p class="brand-name">Keystone Ladder<br>Method</p>

</main>
</body>
</html>
```